Kem7Dex Letterhead

Need a new letterhead for my law firm.
IDENTIFYING INFORMATION BELOW:
Ansel T Brightwater III
Attorney at Law
Address: 4832 Tillbury Rd, Ste 250, Dallas, TX 75204
Phone: 866-402-7183
Fax: 469-583-0271
Email: kem@kem7dex.example
Website: www.kem7dex.example

Colors
0054AA
0677BA
7BADD7
CADEEF
E8F1F8

Requirements
Must have
• Logo needs to be on the letterhead, along with identifying information which is included in the project description.

```html
<!DOCTYPE html>
<html lang="en">
<head>
<meta charset="utf-8">
<title>Kem7Dex Letterhead</title>
<link href="https://fonts.googleapis.com/css2?family=Montserrat:wght@400;500;700;800&display=swap" rel="stylesheet">
<style>
  :root {
    --blue-deep: #0054AA;
    --blue-mid: #0677BA;
    --blue-bright: #1a9ad6;
    --blue-soft: #7BADD7;
    --blue-pale: #CADEEF;
    --blue-mist: #E8F1F8;
    --ink: #141414;
    --paper: #ffffff;
    --backdrop: #e6edf4;
  }
  * { box-sizing: border-box; margin: 0; padding: 0; }
  html, body {
    width: 1200px; height: 898px; overflow: hidden;
    background: var(--backdrop);
    font-family: "Montserrat", Arial, sans-serif;
  }
  .letterhead {
    position: absolute; left: 290px; top: 48px;
    width: 620px; height: 802px;
    background: var(--paper);
    box-shadow: 0 6px 24px rgba(0, 40, 90, 0.18);
    overflow: hidden;
  }
  .header-art { position: absolute; left: 0; top: 0; }
  .brand-name {
    position: absolute; left: 34px; top: 60px;
    font-weight: 800; font-size: 32px; letter-spacing: 0.5px;
    color: var(--ink);
  }
  .attorney {
    position: absolute; right: 24px; top: 40px; text-align: right;
    color: var(--paper);
  }
  .attorney-name { font-weight: 700; font-size: 12.5px; letter-spacing: 1.4px; text-transform: uppercase; }
  .attorney-title { font-weight: 400; font-size: 10.5px; letter-spacing: 1.2px; text-transform: uppercase; margin-top: 4px; color: var(--blue-mist); }
  .footer-art { position: absolute; left: 0; bottom: 0; }
  .website {
    position: absolute; left: 0; right: 0; bottom: 78px; text-align: center;
    font-weight: 700; font-size: 11px; letter-spacing: 1px; color: var(--paper);
  }
  .contact-row {
    position: absolute; left: 18px; right: 14px; bottom: 20px;
    display: flex; justify-content: space-between; align-items: center;
  }
  .contact-item { display: flex; align-items: center; gap: 6px; color: var(--paper); font-size: 8.6px; font-weight: 500; }
  .contact-icon {
    width: 20px; height: 20px; border-radius: 50%; background: var(--paper);
    display: flex; align-items: center; justify-content: center; flex: none;
  }
</style>
</head>
<body>
  <main class="letterhead">
    <svg class="header-art" width="620" height="130" viewBox="0 0 620 130" aria-hidden="true">
      <defs>
        <linearGradient id="band-left" x1="0" x2="1" y1="0" y2="0">
          <stop offset="0" stop-color="#0054AA"/>
          <stop offset="1" stop-color="#1a9ad6"/>
        </linearGradient>
        <linearGradient id="band-right" x1="0" x2="1" y1="0" y2="0">
          <stop offset="0" stop-color="#1a9ad6"/>
          <stop offset="0.7" stop-color="#0677BA"/>
          <stop offset="1" stop-color="#0054AA"/>
        </linearGradient>
        <linearGradient id="slash" x1="0" x2="1" y1="0" y2="1">
          <stop offset="0" stop-color="#1a9ad6"/>
          <stop offset="1" stop-color="#0054AA"/>
        </linearGradient>
      </defs>
      <polygon points="0,30 292,30 302,48 0,48" fill="url(#band-left)"/>
      <polygon points="0,48 302,48 304,51 0,51" fill="#0054AA"/>
      <polygon points="226,58 258,58 298,102 266,102" fill="url(#slash)"/>
      <polygon points="276,64 302,64 342,110 316,110" fill="url(#slash)"/>
      <polygon points="312,28 620,28 620,92 356,92" fill="url(#band-right)"/>
    </svg>
    <div class="brand-name">Kem7Dex</div>
    <div class="attorney">
      <div class="attorney-name">Ansel T Brightwater III</div>
      <div class="attorney-title">Attorney at Law</div>
    </div>

    <svg class="footer-art" width="620" height="130" viewBox="0 0 620 130" aria-hidden="true">
      <defs>
        <linearGradient id="footer-band" x1="0" x2="1" y1="0" y2="0">
          <stop offset="0" stop-color="#0054AA"/>
          <stop offset="0.45" stop-color="#1a9ad6"/>
          <stop offset="1" stop-color="#0054AA"/>
        </linearGradient>
      </defs>
      <path d="M0,40 Q310,22 620,4 L620,130 L0,130 Z" fill="url(#footer-band)"/>
      <path d="M0,72 Q330,58 620,34" fill="none" stroke="#ffffff" stroke-width="3"/>
    </svg>
    <div class="website">www.kem7dex.example</div>
    <div class="contact-row">
      <div class="contact-item">
        <span class="contact-icon"><svg width="11" height="11" viewBox="0 0 24 24"><path fill="#0054AA" d="M6.6 10.8a15 15 0 0 0 6.6 6.6l2.2-2.2a1 1 0 0 1 1-.25 11.4 11.4 0 0 0 3.6.57 1 1 0 0 1 1 1V20a1 1 0 0 1-1 1A17 17 0 0 1 3 4a1 1 0 0 1 1-1h3.5a1 1 0 0 1 1 1c0 1.25.2 2.45.57 3.57a1 1 0 0 1-.25 1z"/></svg></span>
        866-402-7183
      </div>
      <div class="contact-item">
        <span class="contact-icon"><svg width="11" height="11" viewBox="0 0 24 24"><rect x="2" y="5" width="20" height="14" rx="2" fill="#0054AA"/><path d="M3 6l9 7 9-7" fill="none" stroke="#fff" stroke-width="2"/></svg></span>
        kem@kem7dex.example
      </div>
      <div class="contact-item">
        <span class="contact-icon"><svg width="11" height="11" viewBox="0 0 24 24"><rect x="6" y="2" width="12" height="6" fill="#0054AA"/><rect x="2" y="9" width="20" height="9" rx="2" fill="#0054AA"/><rect x="6" y="14" width="12" height="8" fill="#0054AA" stroke="#fff" stroke-width="1.5"/></svg></span>
        469-583-0271
      </div>
      <div class="contact-item">
        <span class="contact-icon"><svg width="11" height="11" viewBox="0 0 24 24"><path fill="#0054AA" d="M12 2a7 7 0 0 0-7 7c0 5.2 7 13 7 13s7-7.8 7-13a7 7 0 0 0-7-7zm0 9.5A2.5 2.5 0 1 1 12 6.5a2.5 2.5 0 0 1 0 5z"/></svg></span>
        4832 Tillbury Rd, Ste 250, Dallas, TX 75204
      </div>
    </div>
  </main>
</body>
</html>
```